Colour consulting and Interior design company needs a squarespace web design

we need a website design for squarespace for a Melbourne based company called 'Brightwell Rooms' which incorporates the existing logo. The company primarily provides colour consulting for residential and commercial as well as interior design services. Schemes are personalised for each client. I would like the design to have some colour and use the colour palette provided but it is not is not totally exclusive. The final design should indicate character, playfulness, functionality , harmony and joy. I like the blue/green core colour with the white and would like that to be incorporated.
as per image provided below - double sided
4 page
- space for some images but not too many.
- Page for booking consultation
- real images of houses

```html
<!DOCTYPE html>
<html lang="en">
<head>
<meta charset="utf-8">
<title>Brightwell Rooms — Colour Consulting &amp; Interior Design</title>
<link href="https://fonts.googleapis.com/css2?family=Libre+Franklin:wght@300;400;500;600&display=swap" rel="stylesheet">
<style>
:root{
  --ink:#0e3340;
  --teal:#1b6c84;
  --teal-deep:#0c3d49;
  --teal-bar:#1e6f88;
  --muted:#5b6b72;
  --panel:#efefef;
  --line:#2c7390;
  --white:#ffffff;
}
*{box-sizing:border-box;margin:0;padding:0}
html,body{width:1200px;height:3681px;overflow:hidden}
body{font-family:"Libre Franklin",Arial,sans-serif;color:var(--ink);background:var(--white);position:relative}
.abs{position:absolute}
a{color:inherit;text-decoration:none}

/* hero */
.hero{left:0;top:0;width:1200px;height:638px;background:linear-gradient(160deg,#8a8178 0%,#6a5a4e 30%,#4a382e 60%,#2c211c 100%)}
.hero-shade{left:0;top:0;width:1200px;height:638px;background:linear-gradient(90deg,rgba(20,14,10,.45) 0%,rgba(20,14,10,.1) 60%,rgba(20,14,10,.2) 100%)}
.brand{left:81px;top:36px;display:flex;align-items:center;gap:12px;color:var(--white);white-space:nowrap}
.brand-mark{width:40px;height:40px;background:var(--white)}
.brand-name{font-size:26px;font-weight:500;letter-spacing:.2px}
.nav{left:568px;top:54px;display:flex;gap:34px;color:var(--white);font-size:14px;white-space:nowrap}
.nav-cta{left:923px;top:47px;width:196px;height:34px;border:1.5px solid var(--white);color:var(--white);font-size:12.5px;display:flex;align-items:center;justify-content:center;white-space:nowrap}
.hero-title{left:81px;top:268px;color:var(--white);font-weight:300;line-height:1.2;white-space:nowrap}
.hero-title .l1{font-size:38px;display:block}
.hero-title .l2{font-size:48px;display:block}
.hero-btn{left:81px;top:400px;width:159px;height:34px;border:1.5px solid var(--white);color:var(--white);font-size:12.5px;display:flex;align-items:center;justify-content:center;white-space:nowrap}
.dots{left:1074px;top:272px;display:flex;flex-direction:column;gap:12px}
.dots span{width:12px;height:12px;border-radius:50%;border:1.5px solid var(--white)}
.dots span.on{background:var(--white)}
.callbar{left:601px;top:601px;width:530px;height:79px;background:var(--teal-bar);color:var(--white);display:flex;align-items:center;padding:0 36px;font-size:19px;white-space:nowrap}
.callbar > *{flex-shrink:0}
.callbar .num{display:flex;align-items:center;gap:8px;margin-left:10px;font-size:21px;font-weight:500}
.callbar .or{margin-left:30px;opacity:.85}
.callbar .btn{margin-left:30px;width:120px;height:36px;background:var(--white);color:var(--teal);font-size:12px;display:flex;align-items:center;justify-content:center}

/* section headings */
.rule{width:42px;height:2px;background:var(--line)}
.lead{font-size:29px;font-weight:500;line-height:1.32;color:var(--ink)}

/* service cards */
.card{top:962px;width:272px;height:351px;overflow:hidden}
.card-photo{width:100%;height:100%}
.card-fade{left:0;bottom:0;width:100%;height:60%;background:linear-gradient(180deg,rgba(12,61,73,0) 0%,rgba(12,61,73,.85) 100%)}
.card-label{left:0;width:100%;bottom:50px;text-align:center;color:var(--white)}
.card-label b{display:block;font-size:29px;font-weight:400}
.card-label small{display:block;font-size:12.5px;margin-top:4px}
.card.lifted{box-shadow:0 26px 40px rgba(0,0,0,.22)}
.card-copy{left:40px;width:192px;top:140px;text-align:center;color:var(--white);font-size:13.5px;line-height:1.5}
.card-more{left:77px;top:256px;width:118px;height:32px;border:1.5px solid var(--white);color:var(--white);font-size:12px;display:flex;align-items:center;justify-content:center}

/* about */
.body-copy{font-size:12.5px;line-height:1.55;color:var(--muted);text-align:justify}
.outline-btn{border:1.5px solid var(--teal);color:var(--teal);font-size:12px;display:flex;align-items:center;justify-content:center;white-space:nowrap}
.play{left:873px;top:1645px}

/* carousel */
.slide{top:2157px;height:479px}
.slide-veil{background:rgba(255,255,255,.62)}
.caption{left:299px;top:2530px;width:602px;text-align:center;color:var(--white)}
.caption b{font-size:21px;font-weight:400;display:block}
.caption small{font-size:12px;display:block;margin-top:6px}
.arrow{top:2382px}

/* contact */
.form-panel{left:601px;top:2756px;width:439px;height:478px;background:var(--panel)}
.field{left:640px;width:359px;background:var(--white);font-size:12px;color:#8a9296;padding:0 22px;display:flex;align-items:center}
.field.area{align-items:flex-start;padding-top:14px}
.submit{left:640px;top:3156px;width:359px;height:39px;background:var(--teal);color:var(--white);font-size:12px;font-weight:500;display:flex;align-items:center;justify-content:space-between;padding:0 22px}

/* footer */
.footer{left:0;top:3357px;width:1200px;height:324px;background:var(--teal-deep);color:var(--white)}
.f-mark{left:81px;top:3426px;width:48px;height:48px;background:#2c7390}
.f-text{font-size:12px;line-height:1.7;color:#c7d6da;white-space:nowrap}
.f-head{font-size:15px;color:var(--white);white-space:nowrap}
.socials{left:768px;top:3506px;display:flex;gap:14px}
.socials span{width:30px;height:30px;border-radius:50%;border:1.5px solid #8fb1ba}
.socials span.on{background:var(--teal);border-color:var(--teal)}
.to-top{left:1065px;top:3440px;width:30px;height:30px;border-radius:50%;background:var(--teal);display:flex;align-items:center;justify-content:center}
</style>
</head>
<body>

<!-- hero -->
<div class="abs hero" role="img" aria-label="Photo of a loft living room with exposed brick wall, grey sofa, timber coffee table and staircase"></div>
<div class="abs hero-shade"></div>
<div class="abs brand"><span class="brand-mark"></span><span class="brand-name">Brightwell Rooms</span></div>
<nav class="abs nav"><a>About</a><a>Interior Design</a><a>Projects</a><a>Contact</a></nav>
<a class="abs nav-cta">Request A Colour Consultant</a>
<h1 class="abs hero-title"><span class="l1">Your Personality. Your Space.</span><span class="l2">Our Inspiraton.</span></h1>
<a class="abs hero-btn">Contact Us Today!</a>
<div class="abs dots"><span></span><span class="on"></span><span></span><span></span><span></span></div>
<div class="abs callbar">
  <span>Call Today!</span>
  <span class="num"><svg width="18" height="18" viewBox="0 0 24 24"><path fill="#fff" d="M6.6 10.8a15.1 15.1 0 0 0 6.6 6.6l2.2-2.2c.3-.3.7-.4 1-.2 1.1.4 2.3.6 3.6.6.6 0 1 .4 1 1V20c0 .6-.4 1-1 1A17 17 0 0 1 3 4c0-.6.4-1 1-1h3.5c.6 0 1 .4 1 1 0 1.3.2 2.5.6 3.6.1.3 0 .7-.2 1z"/></svg>0412 555 018</span>
  <span class="or">or</span>
  <a class="btn">Contact Us</a>
</div>

<!-- intro -->
<div class="abs rule" style="left:81px;top:810px"></div>
<p class="abs lead" style="left:160px;top:788px;width:680px">Brightwell Rooms provides full service of colour consulting for residential and commercial as well as interior design services.</p>

<div class="abs card" style="left:160px">
  <div class="card-photo" role="img" aria-label="Photo of a modern glass and concrete house among trees" style="background:linear-gradient(160deg,#6f8fb5 0%,#8aa0a8 35%,#4f6a52 70%,#2e4434 100%)"></div>
  <div class="abs card-fade"></div>
  <div class="abs card-label"><b>Residential</b><small>Interior Design</small></div>
</div>
<div class="abs card lifted" style="left:464px">
  <div class="card-photo" role="img" aria-label="Photo of glass office towers against the sky" style="background:linear-gradient(180deg,#b9cbd6 0%,#7d9cb0 45%,#3a6a86 80%,#1d5068 100%)"></div>
  <p class="abs card-copy">Interior design is part of a company's marketing strategy.</p>
  <a class="abs card-more">More Info</a>
</div>
<div class="abs card" style="left:768px">
  <div class="card-photo" role="img" aria-label="Photo of a burst of green and yellow colour powder on a dark background" style="background:radial-gradient(circle at 50% 35%,#c9d94a 0%,#5fae63 28%,#1f6f74 55%,#0d2f45 85%)"></div>
  <div class="abs card-fade"></div>
  <div class="abs card-label"><b>Colour</b><small>Consulting Experts</small></div>
</div>

<!-- about -->
<div class="abs rule" style="left:81px;top:1520px"></div>
<h2 class="abs lead" style="left:160px;top:1498px;width:400px">Brightwell Rooms Personalised Haemonious Design</h2>
<p class="abs body-copy" style="left:160px;top:1622px;width:272px">Lorem ipsum dolor sit amet, consectetur adipiscing elit. Alias voluptate ad velit perspiciatis ipsa! Nostrum voluptate ex at laborum esse culpa modi, molestiae eveniet numquam tenetur expedita quis aspernatur doloribus! Lorem ipsum dolor sit amet, consectetur adipisicing elit. Alias voluptate ad velit perspiciatis ipsa!</p>
<a class="abs outline-btn" style="left:160px;top:1794px;width:120px;height:32px">About Us</a>
<div class="abs" role="img" aria-label="Photo of two designers reviewing colour swatches at a table" style="left:601px;top:1436px;width:599px;height:476px;background:linear-gradient(120deg,#7e7670 0%,#b3aca6 35%,#a09284 60%,#5d5650 100%)"></div>
<svg class="abs play" width="52" height="52" viewBox="0 0 52 52"><circle cx="26" cy="26" r="23" fill="none" stroke="#fff" stroke-width="3"/><path d="M21 16l16 10-16 10z" fill="#fff"/></svg>

<!-- work -->
<div class="abs rule" style="left:81px;top:2044px"></div>
<h2 class="abs lead" style="left:160px;top:2022px;width:700px">Take a look at our work. We value classic design and creative solutions.</h2>
<div class="abs slide" style="left:0;width:267px;background:linear-gradient(160deg,#e8e2dc,#b9aca3 60%,#d9d3cd)" role="img" aria-label="Photo of a bright white living room with pendant lamp"></div>
<div class="abs slide slide-veil" style="left:0;width:267px"></div>
<div class="abs slide" style="left:299px;width:602px;background:linear-gradient(165deg,#c6d6e0 0%,#8faabd 35%,#4d7693 65%,#25506c 100%)" role="img" aria-label="Photo looking up at glass skyscrapers"></div>
<div class="abs caption"><b>Circa Late 1800's Queenslander</b><small>This stunning Queenslander built in 1800's</small></div>
<div class="abs slide" style="left:932px;width:268px;background:linear-gradient(160deg,#d8d2cb,#a89c92 55%,#cfc8c1)" role="img" aria-label="Photo of a white loft lounge with floor lamp"></div>
<div class="abs slide slide-veil" style="left:932px;width:268px"></div>
<svg class="abs arrow" style="left:110px" width="20" height="32" viewBox="0 0 20 32"><path d="M15 4L5 16l10 12" fill="none" stroke="#1b6c84" stroke-width="3"/></svg>
<svg class="abs arrow" style="left:1068px" width="20" height="32" viewBox="0 0 20 32"><path d="M5 4l10 12L5 28" fill="none" stroke="#1b6c84" stroke-width="3"/></svg>

<!-- contact -->
<div class="abs rule" style="left:81px;top:2906px"></div>
<h2 class="abs lead" style="left:160px;top:2884px;width:360px">Have a Question or looking for advice?</h2>
<p class="abs body-copy" style="left:160px;top:2975px;width:280px;text-align:left">We'd love to hear from you! We can cover Interior Decorating, Visual Styling or Colour Consulting and more.</p>
<a class="abs outline-btn" style="left:160px;top:3065px;width:120px;height:32px">Contact Us</a>
<div class="abs form-panel"></div>
<div class="abs field" style="top:2797px;height:40px">Enter your Name</div>
<div class="abs field" style="top:2854px;height:39px">Email</div>
<div class="abs field" style="top:2913px;height:39px">Phone</div>
<div class="abs field area" style="top:2969px;height:167px">Message ...</div>
<a class="abs submit"><span>Consult Now!</span><span>+</span></a>

<!-- footer -->
<footer class="abs footer"></footer>
<div class="abs f-mark"></div>
<div class="abs f-head" style="left:160px;top:3434px">Brightwell Rooms</div>
<div class="abs" style="left:160px;top:3466px;display:flex;align-items:center;gap:8px;color:#fff;font-size:20px;white-space:nowrap"><span>Call Today!</span><svg width="16" height="16" viewBox="0 0 24 24"><path fill="#fff" d="M6.6 10.8a15.1 15.1 0 0 0 6.6 6.6l2.2-2.2c.3-.3.7-.4 1-.2 1.1.4 2.3.6 3.6.6.6 0 1 .4 1 1V20c0 .6-.4 1-1 1A17 17 0 0 1 3 4c0-.6.4-1 1-1h3.5c.6 0 1 .4 1 1 0 1.3.2 2.5.6 3.6.1.3 0 .7-.2 1z"/></svg><span>0412 555 018</span></div>
<div class="abs f-text" style="left:160px;top:3496px">e. hello@brightwellrooms.com</div>
<div class="abs f-text" style="left:160px;top:3534px">Location<br>48 Larch Lane, Southbank,<br>VIC 3006</div>
<div class="abs f-head" style="left:599px;top:3434px">Quick Link</div>
<div class="abs f-text" style="left:599px;top:3458px">About<br>Interior Design<br>Projects<br>Contact</div>
<div class="abs f-head" style="left:768px;top:3434px">© 2018 Brightwell Rooms.</div>
<div class="abs f-text" style="left:768px;top:3460px">All rights reserved.</div>
<div class="abs socials"><span></span><span class="on"></span><span></span><span></span></div>
<div class="abs to-top"><svg width="12" height="8" viewBox="0 0 12 8"><path d="M1 7l5-5 5 5" fill="none" stroke="#fff" stroke-width="2"/></svg></div>

</body>
</html>
```